Hollowmere Estate Premium E-Liquid

We need a business card design, and soon web design/flyers/brochures for a new ELiquid line (for the vaping/ecig market) called Hollowmere Estate. Attached is the basis of our logo and also the "label" that goes on our bottle. Our first flavor out is Q'Vesta. The Final design should be reminiscent of a fine wine label / Whiskey label, that communicates an elegant experience. The information on these cards is strictly generic / wholesale information and will be included in samples sent to shops.

Target Market(s)

E cigarettes / Vaping / Middle to upper class

Industry/Entity Type

Business

Contact Information for Business Card

Would like to include Darren Whitlaw as Founder. Contact is Darren@hollowmereestate-example.com as well as the website of www.hollowmereestate-example.com and a phone number of (555) 718-2964

Number of Pages Required

2 page

Requirements
Must have
• I think the original font in our PSD attached file is what we want across the board. Think "old school tonic" or "Wine labels". Classy/elegant/"high end".
Nice to have
• Would also like to do a card in the same finished design but it would strictly have the company and whole sale information. This would be sent out with samples.
• And then say for wholesale contact sales: sales@hollowmereestate-example.com or visit hollowmereestate-example.com

```html
<!DOCTYPE html>
<html lang="en">
<head>
<meta charset="utf-8">
<title>Hollowmere Estate – Business Cards</title>
<link rel="stylesheet" href="https://fonts.googleapis.com/css2?family=Cinzel:wght@400&family=Crimson+Text:wght@400&display=swap">
<style>
  :root {
    --page-bg: #ecebe7;
    --card-light: #ebe3cf;
    --card-mid: #e0d5bb;
    --card-edge: #cfc2a3;
    --ink: #1d1b18;
    --accent: #b4553a;
  }
  * { margin: 0; padding: 0; box-sizing: border-box; }
  html, body { width: 1200px; height: 900px; overflow: hidden; }
  body {
    background: var(--page-bg);
    display: flex;
    align-items: center;
    justify-content: center;
    gap: 44px;
  }
  .card {
    position: relative;
    width: 540px;
    height: 308px;
    background: radial-gradient(ellipse at 50% 45%, var(--card-light) 0%, var(--card-mid) 75%, var(--card-edge) 100%);
    box-shadow: 0 2px 6px rgba(0,0,0,0.18);
    color: var(--ink);
  }
  .card__frame {
    position: absolute;
    inset: 0;
    width: 100%;
    height: 100%;
  }
  .card__content {
    position: absolute;
    inset: 0;
    display: flex;
    flex-direction: column;
    align-items: center;
    justify-content: center;
    text-align: center;
  }
  .ornament {
    width: 96px;
    height: 26px;
    background: linear-gradient(90deg, rgba(29,27,24,0) 0%, rgba(29,27,24,0.55) 50%, rgba(29,27,24,0) 100%);
    border-radius: 50%;
    margin-bottom: 10px;
  }
  .rule {
    height: 2px;
    background: var(--ink);
  }
  .rule--wide { width: 250px; }
  .rule--narrow { width: 220px; }
  .brand-name {
    font-family: "Cinzel", serif;
    font-weight: 400;
    font-size: 26px;
    line-height: 1.12;
    letter-spacing: 0.5px;
    margin: 8px 0 10px;
  }
  .website, .contact {
    font-family: "Crimson Text", serif;
    font-size: 14px;
    line-height: 1.2;
  }
  .card--front .website { margin-top: 9px; }
  .person-name {
    font-family: "Crimson Text", serif;
    font-size: 15px;
    line-height: 1.1;
    margin-top: 8px;
  }
  .person-role {
    font-family: "Crimson Text", serif;
    font-size: 12px;
    color: var(--accent);
    margin-bottom: 8px;
  }
</style>
</head>
<body>

  <section class="card card--front">
    <svg class="card__frame" viewBox="0 0 540 308" aria-hidden="true">
      <ellipse cx="270" cy="154" rx="228" ry="120" fill="none" stroke="#1d1b18" stroke-width="2.5"/>
      <ellipse cx="270" cy="154" rx="221" ry="113" fill="none" stroke="#1d1b18" stroke-width="1"/>
    </svg>
    <div class="card__content">
      <div class="ornament" role="img" aria-label="Decorative fleur-de-lis flourish"></div>
      <div class="rule rule--wide"></div>
      <h1 class="brand-name">Hollowmere<br>Estate</h1>
      <div class="rule rule--narrow"></div>
      <p class="website">www.hollowmereestate-example.com</p>
    </div>
  </section>

  <section class="card card--back">
    <svg class="card__frame" viewBox="0 0 540 308" aria-hidden="true">
      <ellipse cx="270" cy="154" rx="228" ry="120" fill="none" stroke="#1d1b18" stroke-width="2.5"/>
      <ellipse cx="270" cy="154" rx="221" ry="113" fill="none" stroke="#1d1b18" stroke-width="1"/>
    </svg>
    <div class="card__content">
      <div class="rule rule--wide"></div>
      <h2 class="brand-name">Hollowmere<br>Estate</h2>
      <div class="rule rule--narrow"></div>
      <p class="person-name">Darren Whitlaw</p>
      <p class="person-role">Founder</p>
      <p class="contact">sales@hollowmereestate-example.com</p>
      <p class="contact">www.hollowmereestate-example.com</p>
    </div>
  </section>

</body>
</html>
```